Laboratory marketing Flyer

I want to create a flyer that's reflective of all the services our laboratory offers. please review our services at www.qorvendiagnostics.com as well as about us for our amenities. focus more on areas of testing other than Toxicology, Covid-19 and Neutralizing anti-body titer. More so on UTI, Gastrointestinal, Wound, Genetics and respiratory. attached is a very old/outdated brochure, I want this in one page, vertical, front and back format.

Target Market(s)

medical facilities

Industry/Entity Type

medical

Font styles to use
Sans Serif

Colors
0054AA
0677BA
7BADD7
CADEEF
E8F1F8

Requirements
Must have
• Answer the phone, quick sample collection, fast turnaround time, large test menu, and Tally-Ward-Link integration

```html
<!DOCTYPE html>
<html lang="en">
<head>
<meta charset="utf-8">
<title>Qorven Diagnostics – Laboratory Flyer, Front and Back</title>
<link href="https://fonts.googleapis.com/css2?family=Montserrat:wght@500;600;700;800&family=Roboto:wght@400;500&display=swap" rel="stylesheet">
<style>
  :root{
    --blue-deep:#0054AA;
    --blue:#0677BA;
    --blue-mid:#7BADD7;
    --blue-soft:#CADEEF;
    --blue-pale:#E8F1F8;
    --ink:#1c1c1c;
    --black:#0b0b0b;
    --white:#ffffff;
    --stage:#e4e4e4;
  }
  *{margin:0;padding:0;box-sizing:border-box}
  html,body{width:828px;height:1200px;overflow:hidden;background:var(--stage)}
  .stage{position:relative;width:828px;height:1200px}
  .sheet{position:absolute;top:325px;width:680px;height:960px;background:var(--white);overflow:hidden;
         transform:scale(0.5735);transform-origin:0 0;font-family:"Roboto",Arial,sans-serif;color:var(--ink);
         box-shadow:0 2px 10px rgba(0,0,0,.18)}
  .sheet-front{left:16px}
  .sheet-back{left:422px}
  .shapes{position:absolute;left:0;top:0}
  .abs{position:absolute}
  .mont{font-family:"Montserrat",Arial,sans-serif}

  /* front */
  .brand{left:0;top:34px;width:340px;text-align:center}
  .brand-dot{width:54px;height:54px;border:5px solid var(--blue-deep);border-radius:50%;margin:0 auto 10px}
  .brand-name{font-family:"Montserrat",Arial,sans-serif;font-weight:800;font-size:28px;line-height:1.12;color:var(--blue-deep)}
  .headline{left:46px;top:198px;width:300px}
  .headline h1{font-family:"Montserrat",Arial,sans-serif;font-weight:800;font-size:27px;line-height:1.1;color:var(--blue)}
  .headline p{margin-top:8px;font-family:"Montserrat",Arial,sans-serif;font-weight:500;font-size:19px;line-height:1.22}
  .promise{left:0;top:360px;width:680px;height:96px;color:var(--white);text-align:center;
           font-family:"Montserrat",Arial,sans-serif;font-weight:600;font-size:20px;line-height:1.17;padding-top:12px}
  .promise strong{font-weight:800}
  .features{left:0;top:474px;width:680px;text-align:center;font-family:"Montserrat",Arial,sans-serif;font-weight:600;font-size:14.5px;line-height:1.45;color:var(--blue)}
  .dot-tick{display:inline-block;width:10px;height:10px;border-radius:50%;background:var(--blue-mid);margin:0 7px;vertical-align:0;position:relative}
  .dot-tick::after{content:"";position:absolute;left:3px;top:1.5px;width:3px;height:5px;border:solid var(--white);border-width:0 1.4px 1.4px 0;transform:rotate(45deg)}
  .about-title{left:88px;top:548px;font-family:"Montserrat",Arial,sans-serif;font-weight:600;font-size:15px;color:var(--white)}
  .about{left:46px;top:588px;width:264px;font-size:11.3px;line-height:1.36}
  .about p+p{margin-top:12px}
  .about p:first-child{font-weight:500}

  /* footer shared */
  .phone{left:48px;top:888px;display:flex;align-items:center;gap:6px;font-family:"Montserrat",Arial,sans-serif;font-weight:700;font-size:33px;color:var(--white)}
  .contact{left:388px;top:876px;font-family:"Montserrat",Arial,sans-serif;font-weight:500;font-size:13px;line-height:1.25;color:var(--white)}
  .contact-row{display:flex;gap:7px;align-items:flex-start}
  .contact-row+.contact-row{margin-top:6px}
  .contact svg{flex:none;margin-top:2px}

  /* back */
  .back-head{left:47px;top:30px;font-family:"Montserrat",Arial,sans-serif;font-weight:700;font-size:16.5px;line-height:1.22}
  .back-head span{color:var(--blue)}
  .service{display:flex;align-items:center;gap:8px;font-family:"Montserrat",Arial,sans-serif;font-weight:500;font-size:10.5px;line-height:1.22;width:140px}
  .service svg{flex:none}
  .benefits-title{left:252px;top:449px;width:185px;text-align:center;font-family:"Montserrat",Arial,sans-serif;font-weight:800;font-size:21px;color:var(--white)}
  .benefit{width:260px}
  .benefit-head{display:flex;gap:8px;align-items:flex-start}
  .benefit-head svg{flex:none;margin-top:-6px}
  .benefit h3{font-family:"Montserrat",Arial,sans-serif;font-weight:500;font-size:13px;line-height:1.12;color:var(--blue)}
  .benefit ul{list-style:none;margin:4px 0 0 28px;font-size:11.2px;line-height:1.34}
  .benefit li{position:relative;padding-left:18px}
  .benefit li+li{margin-top:2px}
  .benefit li.gap{margin-top:14px}
  .benefit li::before{content:"";position:absolute;left:0;top:3px;width:9px;height:9px;border-radius:50%;background:var(--blue)}
  .benefit li::after{content:"";position:absolute;left:3px;top:4.5px;width:2.5px;height:4.5px;border:solid var(--white);border-width:0 1.3px 1.3px 0;transform:rotate(45deg)}
  .back-name{left:420px;top:792px;width:200px;text-align:center;font-family:"Montserrat",Arial,sans-serif;font-weight:800;font-size:22px;color:var(--blue-deep)}
</style>
</head>
<body>
<main class="stage">

  <!-- FRONT -->
  <section class="sheet sheet-front">
    <svg class="shapes" width="680" height="960" viewBox="0 0 680 960">
      <defs>
        <linearGradient id="frontLab" x1="0" y1="0" x2="1" y2="1">
          <stop offset="0" stop-color="#e2eaf2"/><stop offset=".55" stop-color="#a9bfd6"/><stop offset="1" stop-color="#5f7fa6"/>
        </linearGradient>
        <linearGradient id="frontResearch" x1="0" y1="0" x2="1" y2="0">
          <stop offset="0" stop-color="#7fa4c8"/><stop offset=".5" stop-color="#cfe2f2"/><stop offset="1" stop-color="#eef4f9"/>
        </linearGradient>
      </defs>
      <polygon points="340,250 510,345 680,250 680,360 340,360" fill="var(--blue-pale)"/>
      <g role="img" aria-label="Photo of a scientist in a protective suit working at a microscope">
        <polygon points="340,0 680,0 680,232 510,328 340,232" fill="url(#frontLab)"/>
      </g>
      <polygon points="340,252 510,348 680,252 680,278 510,374 340,278" fill="var(--blue-deep)"/>
      <rect x="0" y="360" width="680" height="96" fill="var(--blue-deep)"/>
      <polygon points="56,544 210,544 202,570 46,570" fill="var(--blue-deep)"/>
      <rect x="46" y="572" width="262" height="2" fill="var(--blue-deep)"/>
      <g role="img" aria-label="Photo of two lab technicians, one at a microscope and one holding blue test tubes">
        <polygon points="340,566 680,522 680,836 340,836" fill="url(#frontResearch)"/>
      </g>
      <rect x="0" y="862" width="680" height="98" fill="var(--black)"/>
      <polygon points="385,862 680,862 680,960 366,960" fill="var(--blue-deep)"/>
    </svg>

    <header class="abs brand">
      <div class="brand-dot"></div>
      <div class="brand-name">QORVEN<br>DIAGNOSTICS</div>
    </header>

    <div class="abs headline">
      <h1>STATE-OF-THE-ART<br>LAB DIAGNOSTICS</h1>
      <p>GET FAST, PRECISE RESULTS<br>THROUGH THE MOST<br>INNOVATIVE TESTING</p>
    </div>

    <div class="abs promise">
      WE PROVIDE OUR PARTNERS WITH INDUSTRY<br>
      <strong>LEADING LESS THAN 30-HOUR TURNAROUND TIME</strong><br>
      FOR QUANTITATIVE RESULTS.
    </div>

    <div class="abs features">
      Answer the phone<span class="dot-tick"></span>quick sample collection<span class="dot-tick"></span>fast turnaround time<br>
      large test menu, and Tally-Ward-Link integration
    </div>

    <h2 class="abs about-title">ABOUT US</h2>
    <div class="abs about">
      <p>At Qorven we strive at providing our patients with the best quality care by providing physicians, hospitals, medical centers, clinics, and healthcare facilities with state-of-the-art urine drug confirmation testing for the most commonly scheduled prescription drugs and narcotics.</p>
      <p>The highly complex method developed by our team will most definitely detect, and confirm the presence and concentration of scheduled prescription drugs and illicit narcotics which will aid your practice in providing a lab-guided medication management program for your patients.</p>
    </div>

    <div class="abs phone">
      <svg width="22" height="30" viewBox="0 0 24 32"><path d="M7 2c-3 1-5 4-5 9 0 8 5 16 11 19 2 1 4 0 5-1l2-3-5-4-2 2c-3-2-5-7-5-11l3-1-1-7z" fill="var(--blue)"/></svg>
      (555) 214-0387
    </div>
    <div class="abs contact">
      <div class="contact-row">
        <svg width="11" height="15" viewBox="0 0 12 16"><path d="M6 0a6 6 0 0 0-6 6c0 4.5 6 10 6 10s6-5.5 6-10a6 6 0 0 0-6-6zm0 8.5A2.5 2.5 0 1 1 6 3.5a2.5 2.5 0 0 1 0 5z" fill="var(--white)"/></svg>
        <span>4120 Meridian Pkwy, Suite 210<br>Lakeview, MI 48000</span>
      </div>
      <div class="contact-row">
        <svg width="12" height="12" viewBox="0 0 14 14"><circle cx="7" cy="7" r="6" fill="none" stroke="var(--white)" stroke-width="1.5"/><path d="M1 7h12M7 1c-3 3-3 9 0 12M7 1c3 3 3 9 0 12" fill="none" stroke="var(--white)" stroke-width="1.2"/></svg>
        <span>www.qorvendiagnostics.com</span>
      </div>
    </div>
  </section>

  <!-- BACK -->
  <section class="sheet sheet-back">
    <svg class="shapes" width="680" height="960" viewBox="0 0 680 960">
      <defs>
        <linearGradient id="backTeam" x1="0" y1="0" x2="1" y2="1">
          <stop offset="0" stop-color="#eef3f8"/><stop offset=".6" stop-color="#b8cde0"/><stop offset="1" stop-color="#7e9cbd"/>
        </linearGradient>
        <linearGradient id="backLab" x1="0" y1="0" x2="1" y2="1">
          <stop offset="0" stop-color="#dde7f1"/><stop offset=".5" stop-color="#a5bed6"/><stop offset="1" stop-color="#6b8db3"/>
        </linearGradient>
      </defs>
      <g role="img" aria-label="Photo of two scientists in lab coats examining test tubes">
        <polygon points="340,0 680,0 680,120 512,200 340,140" fill="url(#backTeam)"/>
      </g>
      <g role="img" aria-label="Photo of a team of researchers working in a bright laboratory">
        <polygon points="340,155 512,214 680,134 680,345 512,430 340,345" fill="url(#backLab)"/>
      </g>
      <polygon points="340,360 512,448 680,360 680,386 512,474 340,386" fill="var(--blue-deep)"/>
      <polygon points="0,800 680,742 680,862 0,862" fill="var(--blue-deep)"/>
      <rect x="32" y="464" width="618" height="398" fill="var(--blue-pale)"/>
      <polygon points="262,446 440,446 430,480 252,480" fill="var(--blue-deep)"/>
      <rect x="0" y="862" width="680" height="98" fill="var(--black)"/>
      <polygon points="385,862 680,862 680,960 366,960" fill="var(--blue-deep)"/>
    </svg>

    <h1 class="abs back-head">ACCURATE, FAST LABORATORY<br>DIAGNOSTIC SERVICES<br><span>FOR MEDICAL PROVIDERS</span></h1>

    <!-- service column 1 -->
    <div class="abs service" style="left:47px;top:113px">
      <svg width="40" height="40" viewBox="0 0 40 40"><circle cx="20" cy="20" r="20" fill="var(--blue-deep)"/><rect x="13" y="11" width="5" height="17" rx="2.5" fill="var(--white)"/><rect x="22" y="11" width="5" height="17" rx="2.5" fill="var(--white)"/></svg>
      <span>Blood Testing</span></div>
    <div class="abs service" style="left:47px;top:161px">
      <svg width="40" height="40" viewBox="0 0 40 40"><circle cx="20" cy="20" r="20" fill="var(--blue-deep)"/><circle cx="20" cy="20" r="7" fill="var(--white)"/><path d="M20 9v22M9 20h22M12 12l16 16M28 12L12 28" stroke="var(--white)" stroke-width="2"/></svg>
      <span>COVID-19<br>Testing</span></div>
    <div class="abs service" style="left:47px;top:210px">
      <svg width="40" height="40" viewBox="0 0 40 40"><circle cx="20" cy="20" r="20" fill="var(--blue-deep)"/><path d="M19 10v10c-3 0-7 3-7 9h6zM21 10v10c3 0 7 3 7 9h-6z" fill="var(--white)"/></svg>
      <span>Respiratory<br>Pathogen Panel<br>(RPP)</span></div>
    <div class="abs service" style="left:47px;top:258px">
      <svg width="40" height="40" viewBox="0 0 40 40"><circle cx="20" cy="20" r="20" fill="var(--blue-deep)"/><circle cx="20" cy="17" r="7" fill="none" stroke="var(--white)" stroke-width="3"/><rect x="18.5" y="23" width="3" height="9" fill="var(--white)"/></svg>
      <span>Women's<br>Health qPCR</span></div>
    <div class="abs service" style="left:47px;top:307px">
      <svg width="40" height="40" viewBox="0 0 40 40"><circle cx="20" cy="20" r="20" fill="var(--blue-deep)"/><circle cx="16" cy="17" r="5" fill="var(--white)"/><circle cx="26" cy="24" r="4" fill="var(--white)"/><circle cx="25" cy="13" r="2.5" fill="var(--white)"/></svg>
      <span>Sexually<br>Transmitted<br>Infections (STI)</span></div>
    <div class="abs service" style="left:47px;top:355px">
      <svg width="40" height="40" viewBox="0 0 40 40"><circle cx="20" cy="20" r="20" fill="var(--blue-deep)"/><rect x="9" y="15" width="22" height="10" rx="5" fill="var(--white)"/><path d="M17 15v10M23 15v10" stroke="var(--blue-deep)" stroke-width="1.5"/></svg>
      <span>Wound Panel</span></div>
    <div class="abs service" style="left:47px;top:403px">
      <svg width="40" height="40" viewBox="0 0 40 40"><circle cx="20" cy="20" r="20" fill="var(--blue-deep)"/><path d="M13 20v-7h3v7M17 19v-9h3v9M21 19v-8h3v8M25 20v-5h3v7c0 5-3 8-8 8s-7-3-7-6z" fill="var(--white)"/></svg>
      <span>Nail Panel</span></div>

    <!-- service column 2 -->
    <div class="abs service" style="left:190px;top:113px">
      <svg width="40" height="40" viewBox="0 0 40 40"><circle cx="20" cy="20" r="20" fill="var(--blue-deep)"/><rect x="11" y="11" width="8" height="18" rx="4" fill="var(--white)"/><circle cx="26" cy="22" r="5" fill="var(--white)"/></svg>
      <span>Toxicology<br>Testing</span></div>
    <div class="abs service" style="left:190px;top:161px">
      <svg width="40" height="40" viewBox="0 0 40 40"><circle cx="20" cy="20" r="20" fill="var(--blue-deep)"/><path d="M20 9l9 4v7c0 6-4 10-9 11-5-1-9-5-9-11v-7z" fill="var(--white)"/><circle cx="20" cy="20" r="3" fill="var(--blue-deep)"/></svg>
      <span>Neutralizing<br>Antibody Titer</span></div>
    <div class="abs service" style="left:190px;top:210px">
      <svg width="40" height="40" viewBox="0 0 40 40"><circle cx="20" cy="20" r="20" fill="var(--blue-deep)"/><rect x="14" y="10" width="12" height="20" rx="1.5" fill="var(--white)"/><path d="M17 15h6M17 19h6M17 23h6" stroke="var(--blue-deep)" stroke-width="1.5"/></svg>
      <span>Urinary Tract<br>Infection qPCR</span></div>
    <div class="abs service" style="left:190px;top:258px">
      <svg width="40" height="40" viewBox="0 0 40 40"><circle cx="20" cy="20" r="20" fill="var(--blue-deep)"/><path d="M13 10h14M13 30h14M14 10c0 6 12 14 12 20M26 10c0 6-12 14-12 20" stroke="var(--white)" stroke-width="2.5" fill="none"/></svg>
      <span>Genetic Testing</span></div>
    <div class="abs service" style="left:190px;top:307px">
      <svg width="40" height="40" viewBox="0 0 40 40"><circle cx="20" cy="20" r="20" fill="var(--blue-deep)"/><circle cx="20" cy="20" r="8" fill="none" stroke="var(--white)" stroke-width="4" stroke-dasharray="5 3"/></svg>
      <span>Infectious<br>Diseases</span></div>
    <div class="abs service" style="left:190px;top:355px">
      <svg width="40" height="40" viewBox="0 0 40 40"><circle cx="20" cy="20" r="20" fill="var(--blue-deep)"/><path d="M18 10v6c-5 0-7 3-7 7 0 5 5 7 9 5 4-2 3-6 7-6v-4c-3 0-5-2-5-4v-4z" fill="var(--white)"/></svg>
      <span>Gastrointestinal<br>Panel</span></div>

    <h2 class="abs benefits-title">OUR BENEFITS</h2>

    <div class="abs benefit" style="left:54px;top:508px">
      <div class="benefit-head">
        <svg width="36" height="36" viewBox="0 0 36 36"><circle cx="18" cy="18" r="16" fill="var(--white)" stroke="var(--blue-deep)" stroke-width="2.5"/><rect x="13" y="10" width="5" height="14" rx="2.5" fill="var(--blue-deep)"/><circle cx="23" cy="21" r="4" fill="var(--blue-deep)"/></svg>
        <h3>Precise results through the most<br>innovative technology</h3>
      </div>
      <ul>
        <li>All of our drug safety monitoring testing will utilize the LC/MS/MS, otherwise known as the “Superior Standard” for analytical quantitation.</li>
        <li class="gap">State-of-the-art method along with precise results means you can trust Qorven to help formulate safety decisions for your patients.</li>
      </ul>
    </div>

    <div class="abs benefit" style="left:54px;top:700px">
      <div class="benefit-head">
        <svg width="36" height="36" viewBox="0 0 36 36"><circle cx="18" cy="18" r="16" fill="var(--white)" stroke="var(--blue-deep)" stroke-width="2.5"/><circle cx="18" cy="18" r="8" fill="none" stroke="var(--blue-deep)" stroke-width="2"/><path d="M18 13v5l3 2" stroke="var(--blue-deep)" stroke-width="2" fill="none"/></svg>
        <h3>PROMPT RESULTS</h3>
      </div>
      <ul>
        <li>We provide our partners with industry leading 48-hour turnaround time for quantitative results.<br>We accomplish this through the optimization of our laboratory testing procedure and by employing the most qualified and experienced laboratory staff.</li>
      </ul>
    </div>

    <div class="abs benefit" style="left:345px;top:508px">
      <div class="benefit-head">
        <svg width="36" height="36" viewBox="0 0 36 36"><circle cx="18" cy="18" r="16" fill="var(--white)" stroke="var(--blue-deep)" stroke-width="2.5"/><rect x="12" y="10" width="12" height="16" rx="1.5" fill="none" stroke="var(--blue-deep)" stroke-width="2"/><path d="M15 22v-3M18 22v-5M21 22v-7" stroke="var(--blue-deep)" stroke-width="2"/></svg>
        <h3>Comprehensive Customized Panels</h3>
      </div>
      <ul>
        <li>We deliver a widespread customizable offering of urine drug testing panels.</li>
      </ul>
    </div>

    <div class="abs benefit" style="left:345px;top:592px">
      <div class="benefit-head">
        <svg width="36" height="36" viewBox="0 0 36 36"><circle cx="18" cy="18" r="16" fill="var(--white)" stroke="var(--blue-deep)" stroke-width="2.5"/><path d="M14 25h10M16 22c0-6 2-8 5-12l2 2c-3 3-4 5-4 10z" fill="var(--blue-deep)" stroke="var(--blue-deep)" stroke-width="1.5"/></svg>
        <h3>Our Amenities</h3>
      </div>
      <ul>
        <li>Tailored collection and pick-up services</li>
        <li>A widespread drug safety testing menu</li>
        <li>Customizable drug testing possibilities</li>
        <li>Remote consultation with our toxicology experts</li>
        <li>Simple, easy-to-read and time sensible reports</li>
        <li>Numerous reporting options</li>
      </ul>
    </div>

    <div class="abs back-name">QORVEN</div>

    <div class="abs phone">
      <svg width="22" height="30" viewBox="0 0 24 32"><path d="M7 2c-3 1-5 4-5 9 0 8 5 16 11 19 2 1 4 0 5-1l2-3-5-4-2 2c-3-2-5-7-5-11l3-1-1-7z" fill="var(--blue)"/></svg>
      (555) 214-0387
    </div>
    <div class="abs contact">
      <div class="contact-row">
        <svg width="11" height="15" viewBox="0 0 12 16"><path d="M6 0a6 6 0 0 0-6 6c0 4.5 6 10 6 10s6-5.5 6-10a6 6 0 0 0-6-6zm0 8.5A2.5 2.5 0 1 1 6 3.5a2.5 2.5 0 0 1 0 5z" fill="var(--white)"/></svg>
        <span>4120 Meridian Pkwy, Suite 210<br>Lakeview, MI 48000</span>
      </div>
      <div class="contact-row">
        <svg width="12" height="12" viewBox="0 0 14 14"><circle cx="7" cy="7" r="6" fill="none" stroke="var(--white)" stroke-width="1.5"/><path d="M1 7h12M7 1c-3 3-3 9 0 12M7 1c3 3 3 9 0 12" fill="none" stroke="var(--white)" stroke-width="1.2"/></svg>
        <span>www.qorvendiagnostics.com</span>
      </div>
    </div>
  </section>

</main>
</body>
</html>
```